BrivoLane Ute.

I want the full logo on one side. And the other side the card if right Ralf the logo the left half orange like the car in the logo color with Danielle R Morrow
Founder and CEO
Email symbol then dmorrow@brivolaneute.com
Www symbol. Then Brivolaneute.com
Phone symbol then 413-926-BRIV
The very bottom would like Brivo Lane Ute is a division of Harmond Vistas. LLC

```html
<!DOCTYPE html>
<html lang="en">
<head>
<meta charset="utf-8">
<title>Brivo Lane Ute – Business Card</title>
<link rel="stylesheet" href="https://fonts.googleapis.com/css2?family=Arimo:wght@400;700&display=swap">
<style>
  :root {
    --bg: #2a2a2c;
    --card-white: #ffffff;
    --brand-orange: #e88a24;
    --ink: #111111;
    --band: #0b0b0b;
    --cream: #f6d9b8;
    --teal: #8fd3c4;
    --text-light: #ffffff;
  }
  * { box-sizing: border-box; margin: 0; padding: 0; }
  html, body {
    width: 1200px; height: 880px; overflow: hidden;
    background: var(--bg);
    font-family: "Arimo", Arial, sans-serif;
  }
  .canvas {
    position: relative; width: 1200px; height: 880px;
    display: flex; flex-direction: column; align-items: center; justify-content: center; gap: 30px;
  }
  .card {
    position: relative; width: 700px; height: 400px;
    border-radius: 26px; overflow: hidden;
    background: var(--card-white);
    box-shadow: 0 14px 30px rgba(0,0,0,.45);
  }

  /* Logo lockup */
  .logo { display: flex; flex-direction: column; align-items: center; }
  .logo-art {
    border-radius: 6px;
    background: linear-gradient(180deg, var(--cream) 0%, #fbe9d2 30%, var(--brand-orange) 55%, #d9791a 75%, var(--teal) 100%);
  }
  .logo-name {
    font-weight: 700; color: var(--ink); text-transform: uppercase;
    letter-spacing: .04em; white-space: nowrap;
  }

  /* Front */
  .card-front { display: flex; align-items: center; justify-content: center; }
  .card-front .logo-art { width: 400px; height: 190px; }
  .card-front .logo-name { font-size: 52px; margin-top: 18px; }

  /* Back */
  .card-back .brand-side {
    position: absolute; left: 0; top: 0; width: 330px; height: 308px;
    display: flex; align-items: center; justify-content: center;
  }
  .card-back .logo-art { width: 230px; height: 110px; }
  .card-back .logo-name { font-size: 27px; margin-top: 12px; }
  .contact-side {
    position: absolute; right: 0; top: 0; width: 370px; height: 100%;
    background: var(--brand-orange); color: var(--text-light);
    padding: 74px 30px 0 40px;
  }
  .person-name { font-size: 24px; font-weight: 700; text-transform: uppercase; }
  .person-title { font-size: 16px; margin-top: 4px; }
  .contact-list { list-style: none; margin-top: 28px; }
  .contact-list li { display: flex; align-items: center; gap: 10px; font-size: 16px; line-height: 1.55; }
  .contact-list svg { width: 14px; height: 14px; fill: var(--text-light); flex: none; }
  .division-band {
    position: absolute; left: 0; right: 0; top: 308px; height: 44px;
    background: var(--band); color: var(--text-light);
    display: flex; align-items: center; justify-content: center;
    font-size: 17px; letter-spacing: .2em;
  }
</style>
</head>
<body>
<main class="canvas">

  <section class="card card-front" aria-label="Card front">
    <div class="logo">
      <div class="logo-art" role="img" aria-label="Illustration of an orange station wagon with a surfboard, wine bottles and a beach fence at sunset"></div>
      <p class="logo-name">Brivo Lane Ute</p>
    </div>
  </section>

  <section class="card card-back" aria-label="Card back">
    <div class="brand-side">
      <div class="logo">
        <div class="logo-art" role="img" aria-label="Illustration of an orange station wagon with a surfboard, wine bottles and a beach fence at sunset"></div>
        <p class="logo-name">Brivo Lane Ute</p>
      </div>
    </div>

    <div class="contact-side">
      <h1 class="person-name">Danielle R Morrow</h1>
      <p class="person-title">Founder and CEO</p>
      <ul class="contact-list">
        <li>
          <svg viewBox="0 0 24 24" aria-hidden="true"><path d="M6.6 10.8a15.1 15.1 0 0 0 6.6 6.6l2.2-2.2c.3-.3.7-.4 1-.2 1.1.4 2.3.6 3.6.6.6 0 1 .4 1 1V20c0 .6-.4 1-1 1A17 17 0 0 1 3 4c0-.6.4-1 1-1h3.5c.6 0 1 .4 1 1 0 1.3.2 2.5.6 3.6.1.3 0 .7-.2 1z"/></svg>
          413-926-BRIV
        </li>
        <li>
          <svg viewBox="0 0 24 24" aria-hidden="true"><path d="M2 5h20v14H2zm2 2v.5l8 5 8-5V7zm0 2.8V17h16V9.8l-8 5z"/></svg>
          dmorrow@brivolaneute.com
        </li>
        <li>
          <svg viewBox="0 0 24 24" aria-hidden="true"><path d="M12 2a10 10 0 1 0 0 20 10 10 0 0 0 0-20zm6.9 9h-3a15 15 0 0 0-1.3-5.6A8 8 0 0 1 18.9 11zM12 4c.9 1.2 1.7 3.6 1.9 7h-3.8c.2-3.4 1-5.8 1.9-7zM9.4 5.4A15 15 0 0 0 8.1 11h-3a8 8 0 0 1 4.3-5.6zM5.1 13h3a15 15 0 0 0 1.3 5.6A8 8 0 0 1 5.1 13zM12 20c-.9-1.2-1.7-3.6-1.9-7h3.8c-.2 3.4-1 5.8-1.9 7zm2.6-1.4a15 15 0 0 0 1.3-5.6h3a8 8 0 0 1-4.3 5.6z"/></svg>
          Brivolaneute.com
        </li>
      </ul>
    </div>

    <p class="division-band">Brivo Lane Ute is a division of Harmond Vistas. LLC</p>
  </section>

</main>
</body>
</html>
```